Accountant and Financial Advisor Client Presentation Folder

We are a medium sized accountancy / taxation and financial advisory firm who has just been through the process of obtaining a new logo and updating our stationary. The last piece of the puzzle is to redesign our existing client presentation folder so that it fits with our new logo (which is black and green).

We want a modern unique image, something creative, but remain professional. Also portray integrity and look approachable. We want to appeal to the younger generation while not losing the respect of our more conservative older clients.

The necessary words and logo to be included on the folder are attached (Presentation Folder Brief), the overall design of the folder is up to you.
We want our new folder to look attractive and stand out from the crowd preferably with a graphic. We have included our old folder which we like (has the dandelion) however the colours etc have now changed as per the black and green mock-up folder example.
We would like a redesign so that we have a graphic to break up the colour. We are open to design changes on the shape of the folder.

Target Market(s)

younger generation while not losing the respect of our more conservative older clients

Industry/Entity Type

Financial

Requirements
Must have
• Graphic in the folder Design

```html
<!DOCTYPE html>
<html lang="en">
<head>
<meta charset="utf-8">
<title>Northridge Accounting – Presentation Folder</title>
<link rel="stylesheet" href="https://fonts.googleapis.com/css2?family=Source+Sans+3:wght@400;600;700&display=swap">
<style>
  :root {
    --charcoal: #333132;
    --lime: #b1d35a;
    --white: #ffffff;
    --paper: #ffffff;
  }
  * { margin: 0; padding: 0; box-sizing: border-box; }
  html, body { width: 1200px; height: 927px; overflow: hidden; background: var(--paper); }
  body { font-family: "Source Sans 3", Arial, sans-serif; }
  .folder { position: relative; width: 1200px; height: 927px; }
  .shapes { position: absolute; inset: 0; }

  .back-panel { position: absolute; left: 18px; top: 122px; width: 419px; height: 572px; background: var(--charcoal); }
  .cover-photo {
    position: absolute; left: 437px; top: 122px; width: 437px; height: 570px;
    background: linear-gradient(180deg, #8d93c2 0%, #b9bdd6 30%, #c9ccd8 44%, #6d7a6a 52%, #5c7a3c 68%, #4d6a2e 84%, #3f5a28 100%);
  }
  .pocket-flap { position: absolute; left: 435px; top: 692px; width: 443px; height: 199px; background: var(--lime); }
  .card-slot { position: absolute; left: 485px; top: 725px; width: 178px; height: 110px; border: 1px solid var(--white); }

  .tagline-block {
    position: absolute; background: var(--lime); color: var(--white);
    font-weight: 600; font-size: 19.5px; line-height: 22.4px; padding: 18px 0 0 17px;
    text-transform: uppercase; letter-spacing: -0.2px;
  }
  .tagline-block--back { left: 279px; top: 122px; width: 131px; height: 179px; }
  .tagline-block--front { left: 462px; top: 121px; width: 130px; height: 177px; }

  .intro { position: absolute; left: 52px; top: 418px; width: 220px; color: var(--white); font-size: 12.3px; line-height: 16.8px; }
  .intro p + p { margin-top: 4px; }
  .intro .accent { color: var(--lime); }

  .services { position: absolute; left: 468px; top: 640px; display: flex; color: var(--white); font-weight: 700; font-size: 9.8px; letter-spacing: -0.1px; }
  .services li { list-style: none; padding: 4px 5px 5px; border-left: 1px solid rgba(255,255,255,0.6); }
  .services li:last-child { border-right: 1px solid rgba(255,255,255,0.6); }

  .services-flipped { position: absolute; left: 640px; top: 725px; width: 198px; transform: rotate(180deg); text-align: left; color: var(--white); font-weight: 700; font-size: 10.5px; line-height: 16.8px; }
  .services-flipped li { list-style: none; }

  .brand { position: absolute; left: 900px; top: 305px; display: flex; align-items: center; gap: 8px; }
  .brand-mark { width: 14px; height: 14px; background: var(--lime); }
  .brand-name { color: var(--white); font-weight: 700; font-size: 19px; letter-spacing: 0.3px; }

  .firm-type { position: absolute; left: 906px; top: 382px; color: var(--white); font-weight: 600; font-size: 16.4px; line-height: 18.5px; }
  .contact { position: absolute; left: 909px; top: 559px; color: var(--white); font-size: 9.6px; line-height: 12.2px; }
  .contact .label { color: var(--lime); }
  .contact .web { color: var(--lime); font-weight: 600; margin-top: 6px; }
</style>
</head>
<body>
<div class="folder">
  <div class="back-panel"></div>
  <div class="cover-photo" role="img" aria-label="Photograph of a hiker standing on a grassy cliff edge overlooking a green river valley under a cloudy sky"></div>
  <div class="pocket-flap"></div>

  <svg class="shapes" width="1200" height="927" viewBox="0 0 1200 927" aria-hidden="true">
    <polygon points="870,122 916,122 1200,344 1074,690 874,690" fill="var(--charcoal)"/>
    <polygon points="216,402 232,402 247,388 253,389 266,364 236,376 241,379" fill="var(--lime)"/>
    <path d="M18,682 C50,660 80,636 104,607 L94,607 C72,632 46,656 18,675 Z" fill="var(--lime)"/>
    <polygon points="551,372 582,378 574,384 632,446 622,455 566,391 559,398" fill="var(--lime)"/>
    <path d="M676,504 C720,560 790,615 874,650 L874,642 C800,610 735,555 686,498 Z" fill="var(--lime)"/>
  </svg>

  <div class="card-slot"></div>

  <div class="tagline-block tagline-block--back">Build<br>your<br>business &amp;<br>grow<br>your<br>wealth</div>
  <div class="tagline-block tagline-block--front">Build<br>your<br>business &amp;<br>grow<br>your<br>wealth</div>

  <div class="intro">
    <p>We are a client focused Accounting Taxation and Financial advisory firm that integrates your personal, business, and financial needs to <span class="accent">provide better outcomes for you.</span></p>
    <p>We see ourselves as your advisor for life <span class="accent">delivering solutions</span> that considers your tax, business finances, superannuation, retirement and investment planning <span class="accent">proactively</span>.</p>
  </div>

  <ul class="services">
    <li>ACCOUNTING</li><li>TAX AGENTS</li><li>FINANCIAL ADVICE</li><li>SELF MANAGED SUPER FUNDS</li>
  </ul>

  <ul class="services-flipped">
    <li>ACCOUNTING</li><li>TAX AGENTS</li><li>FINANCIAL ADVICE</li><li>SELF MANAGED SUPER FUNDS</li>
  </ul>

  <div class="brand"><span class="brand-mark"></span><span class="brand-name">Northridge Accounting</span></div>

  <div class="firm-type">CPA Accounting, Taxation<br>and Financial Advisory Firm</div>

  <div class="contact">
    <div>Suite 8 / 41 Harbour View Road</div>
    <div>PO Box 1120, Alder Bay NSW 2999</div>
    <div><span class="label">P:</span>&nbsp; (02) 5550 1846</div>
    <div><span class="label">E:</span>&nbsp; hello@northridgeacc.example</div>
    <div class="web">www.northridgeacc.example</div>
  </div>
</div>
</body>
</html>
```